insert for clam shell / vape cartridge

Brand : Brevor (roman god of fire)
card insert dimensions are 2.5" in width and 3.375" in height
this is a cannabis product. Open to any and all designs. Currently using very generic text. 5/8" on left edge of design will be covered by the cartridge

Target Market(s)

medical cannabis patients

Industry/Entity Type

Product

Logo Text

Brevor

Requirements
Must have
• logo
Nice to have
• "distilled cannabis oil"
• "no pg/vg"
• subtle use of cannabis leaf
Should not have
• no big (prominent) Pot leaves

```html
<!DOCTYPE html>
<html lang="en">
<head>
<meta charset="utf-8">
<title>Brevor Vapor – Cartridge Insert</title>
<link rel="stylesheet" href="https://fonts.googleapis.com/css2?family=Exo+2:wght@600;700;800&family=Tinos:wght@700&display=swap">
<style>
  :root {
    --plum: #9b1f63;
    --magenta: #e0188f;
    --gold: #d9b23a;
    --flame: #f28c28;
    --yellow: #f7e41c;
    --orange: #f2652b;
    --ink: #111111;
    --paper: #ffffff;
  }
  * { margin: 0; padding: 0; box-sizing: border-box; }
  html, body { width: 949px; height: 1200px; overflow: hidden; background: var(--paper); }
  .insert {
    position: relative;
    width: 949px;
    height: 1200px;
    overflow: hidden;
    background: var(--paper);
    font-family: "Exo 2", sans-serif;
  }
  .brand-panel {
    position: absolute;
    left: 0; top: 0;
    width: 949px; height: 785px;
    background: var(--plum);
  }
  .dot-texture {
    position: absolute;
    left: 0; top: 0;
    width: 420px; height: 785px;
    background: radial-gradient(ellipse 340px 380px at 0% 48%, rgba(224,24,143,0.9) 0%, rgba(224,24,143,0.45) 45%, rgba(224,24,143,0) 100%);
  }
  .mascot-art {
    position: absolute;
    left: 358px; top: 48px;
    width: 515px; height: 445px;
    background: linear-gradient(180deg, rgba(242,140,40,0.55) 0%, rgba(217,178,58,0.8) 35%, rgba(200,160,50,0.85) 100%);
    border-radius: 36px;
  }
  .brand-name {
    position: absolute;
    left: 409px; top: 512px;
    width: 370px;
    text-align: center;
    color: var(--paper);
    font-weight: 800;
    line-height: 1;
  }
  .brand-name .word { display: block; font-size: 90px; letter-spacing: 3px; }
  .brand-name .sub { display: block; font-size: 46px; letter-spacing: 5px; margin-top: 16px; }
  .product-type {
    position: absolute;
    left: 258px; top: 698px;
    width: 700px;
    text-align: center;
    font-family: "Tinos", serif;
    font-weight: 700;
    font-size: 46px;
    letter-spacing: 3px;
    color: var(--yellow);
  }
  .wave-field {
    position: absolute;
    left: 0; top: 785px;
    width: 949px; height: 415px;
    background: linear-gradient(160deg, var(--paper) 0%, #f1f1f1 30%, var(--paper) 55%, #ececec 80%, var(--paper) 100%);
  }
  .flavour {
    position: absolute;
    left: 268px; top: 796px;
    width: 680px;
    text-align: center;
    color: var(--orange);
    font-weight: 700;
    line-height: 1;
  }
  .flavour .line-one { display: block; font-size: 120px; letter-spacing: 6px; }
  .flavour .line-two { display: block; font-size: 98px; letter-spacing: 5px; margin-top: 4px; }
  .spec {
    position: absolute;
    left: 288px;
    width: 640px;
    text-align: center;
    color: var(--ink);
    font-weight: 600;
    line-height: 1;
  }
  .spec-carrier { top: 1014px; font-size: 50px; letter-spacing: 1px; }
  .spec-weight { top: 1072px; font-size: 42px; letter-spacing: 1px; }
  .batch-line {
    position: absolute;
    left: 322px; top: 1138px;
    width: 575px;
    display: flex;
    justify-content: space-between;
    font-size: 33px;
    font-weight: 600;
    letter-spacing: 0.5px;
    color: var(--ink);
  }
</style>
</head>
<body>
<main class="insert">
  <section class="brand-panel">
    <div class="dot-texture" role="img" aria-label="Soft magenta halftone glow"></div>
    <div class="mascot-art" role="img" aria-label="Brand mascot artwork area in gold and flame orange"></div>
    <h1 class="brand-name"><span class="word">BREVOR</span><span class="sub">VAPOR</span></h1>
    <p class="product-type">Distilled Canabis Oil</p>
  </section>
  <section class="wave-field" role="img" aria-label="Soft grey flowing line pattern"></section>
  <h2 class="flavour"><span class="line-one">CITRUS</span><span class="line-two">BURST</span></h2>
  <p class="spec spec-carrier">No PG or VG</p>
  <p class="spec spec-weight">1 gram</p>
  <p class="batch-line"><span>Batch No. 0000000</span><span>THC 70.3%</span></p>
</main>
</body>
</html>
```